Electrician Business needs flyer for discount offer and advertise services

Need a promotional flyer that will grab attention,, offer:

During the months of October & November receive a 10% discount on;
Ceiling fan installation
Smoke alarm installation
Replace existing downlights for new LED downlights.
Offer expires 30th November 2016
'Keep cool, stay safe and save power with VoltMate'

Would like to advertise services and quality on reverse-side. Can have graphic pointing to reverse side on both sides, encouraging customer to read both sides of flyer.
Contact details both sides
Design to suit two-sided A5

Reverse side list services;

All residential & commercial electrical services
Electrical contracting
Real estate/strata electrical maintenance & repairs
New builds
Renovations
Security sensor lighting
Ceiling fans
Smoke Alarms
Data connections

Target Market(s)

Residential home owners and commercial, building and construction companies

Industry/Entity Type

Electrical

Font styles to use
Serif

Colors
0255a3
ffffff

Requirements
Nice to have
• A picture of a modern ceiling fan.
• Arrow/graphic pointing to reverse side, so customer reads both sides of flyer

```html
<!DOCTYPE html>
<html lang="en">
<head>
<meta charset="utf-8">
<title>VoltMate Flyer</title>
<link rel="stylesheet" href="https://fonts.googleapis.com/css2?family=Open+Sans:wght@400;600;700;800&display=swap">
<style>
  :root {
    --brand-blue: #2f5094;
    --accent-orange: #e07b2a;
    --paper: #ffffff;
    --canvas: #ffffff;
    --photo-light: #e4e3df;
    --photo-mid: #cfcdc8;
    --device-light: #f4f4f4;
    --device-mid: #d9d9d9;
  }
  * { box-sizing: border-box; margin: 0; padding: 0; }
  html, body {
    width: 1200px; height: 845px; overflow: hidden;
    background: var(--canvas);
    font-family: "Open Sans", Arial, sans-serif;
  }
  .canvas { position: relative; width: 1200px; height: 845px; }

  .flyer {
    position: absolute; top: 20px; width: 572px; height: 810px;
    box-shadow: 3px 4px 8px rgba(0,0,0,0.35);
    overflow: hidden;
  }

  /* Front side */
  .flyer--front { left: 20px; background: var(--brand-blue); color: var(--paper); }
  .front-header {
    height: 92px; display: flex; align-items: center; justify-content: center; gap: 8px;
  }
  .brand-mark { width: 12px; height: 12px; border-radius: 50%; background: var(--paper); }
  .brand-name { font-weight: 700; font-size: 22px; color: var(--paper); }
  .fan-photo {
    height: 210px;
    background: linear-gradient(180deg, var(--photo-light), var(--photo-mid));
  }
  .offer { text-align: center; padding-top: 26px; }
  .offer-intro {
    font-size: 15px; letter-spacing: 3px; line-height: 20px; text-transform: uppercase;
  }
  .offer-percent { font-size: 44px; font-weight: 800; letter-spacing: 3px; margin-top: 20px; line-height: 50px; }
  .offer-word { font-size: 48px; font-weight: 400; letter-spacing: 7px; line-height: 58px; }
  .offer-items {
    list-style: none; text-align: left; margin: 22px 0 0 117px;
    font-size: 16px; letter-spacing: 2.5px; line-height: 20px; text-transform: uppercase;
  }
  .offer-items li { padding-left: 0; }
  .offer-items .cont { padding-left: 13px; }
  .offer-expiry {
    position: absolute; left: 128px; top: 682px;
    font-size: 8.5px; font-weight: 700; letter-spacing: 1.5px; text-transform: uppercase;
  }
  .turn-badge {
    position: absolute; left: 440px; top: 602px; width: 92px; height: 92px;
    border-radius: 50%; background: var(--accent-orange);
    box-shadow: -3px 4px 6px rgba(0,0,0,0.3);
  }
  .turn-badge svg { position: absolute; left: 24px; top: 14px; }
  .turn-badge-label {
    position: absolute; width: 100%; top: 68px; text-align: center;
    font-size: 8px; font-style: italic; letter-spacing: 1px; text-transform: uppercase;
  }
  .tagline {
    position: absolute; left: 0; right: 0; top: 726px; text-align: center;
    font-size: 18px; font-weight: 700; letter-spacing: 3px; line-height: 23px; text-transform: uppercase;
  }

  /* Reverse side */
  .flyer--back { left: 616px; background: var(--paper); }
  .back-header {
    height: 228px; background: var(--brand-blue);
    display: flex; align-items: center; justify-content: center; gap: 16px;
  }
  .back-header .brand-mark { width: 36px; height: 36px; }
  .back-header .brand-name { font-size: 66px; }
  .services-band {
    height: 88px; background: var(--accent-orange); color: var(--paper);
    display: flex; align-items: center; justify-content: center; text-align: center;
    font-size: 21px; font-weight: 700; letter-spacing: 4px; line-height: 26px; text-transform: uppercase;
  }
  .service-list {
    list-style: none; text-align: center; color: var(--brand-blue); margin-top: 40px;
    font-size: 15px; letter-spacing: 3px; line-height: 16px; text-transform: uppercase;
  }
  .service-list li { margin-bottom: 16px; }
  .alarm-photo {
    position: absolute; left: 232px; top: 662px; width: 148px; height: 148px; border-radius: 50%;
    background: radial-gradient(circle, var(--device-light) 40%, var(--device-mid));
  }
</style>
</head>
<body>
<main class="canvas">
  <section class="flyer flyer--front">
    <header class="front-header">
      <span class="brand-mark"></span>
      <span class="brand-name">VoltMate</span>
    </header>
    <div class="fan-photo" role="img" aria-label="Photo of a modern ceiling fan with wooden blades"></div>
    <div class="offer">
      <p class="offer-intro">During the months<br>of October and November<br>receive a</p>
      <p class="offer-percent">10%</p>
      <p class="offer-word">DISCOUNT</p>
      <ul class="offer-items">
        <li>-Ceiling fan installation</li>
        <li>-Install smoke alarms</li>
        <li>-Replace existing lights for</li>
        <li class="cont">new LED downlights.</li>
      </ul>
    </div>
    <p class="offer-expiry">Offer expires November 30, 2016</p>
    <div class="turn-badge">
      <svg width="44" height="44" viewBox="0 0 44 44" aria-hidden="true">
        <path d="M6 38 C6 20 14 14 26 14 V4 L42 20 L26 36 V26 C16 26 10 30 6 38 Z" fill="#ffffff"/>
      </svg>
      <span class="turn-badge-label">View more</span>
    </div>
    <p class="tagline">Keep cool, stay safe and<br>save power with VoltMate</p>
  </section>

  <section class="flyer flyer--back">
    <header class="back-header">
      <span class="brand-mark"></span>
      <span class="brand-name">VoltMate</span>
    </header>
    <div class="services-band">All residential and commercial<br>electrical services</div>
    <ul class="service-list">
      <li>-Electrical</li>
      <li>-Real estate / strata electrical<br>maintenance and repairs</li>
      <li>-New builds</li>
      <li>-Renovations</li>
      <li>-Safety light sensor</li>
      <li>-Ceiling fans</li>
      <li>-Smoke alarms</li>
      <li>-Data for compounds</li>
    </ul>
    <div class="alarm-photo" role="img" aria-label="Photo of a white ceiling smoke alarm"></div>
  </section>
</main>
</body>
</html>
```